Brindlewood Terrain, LLC Business Card Updates
Oil and Gas Land Services/ A Full Service Land Management Company/ Mineral Owner Consultation and Re
Use same font as used in my logo
Gavin Ressler
Petroleum Landman
426 West Orchard Lane
North Canton, OH 44720
gavin.r.ressler@quellmail.net
No website on this

```html
<!DOCTYPE html>
<html lang="en">
<head>
<meta charset="utf-8">
<title>Brindlewood Terrain, LLC – Business Card</title>
<link rel="stylesheet" href="https://fonts.googleapis.com/css2?family=Michroma&display=swap">
<style>
  :root {
    --page-bg: #e9e7e3;
    --card-bg: #ffffff;
    --ink: #2f2f2f;
    --ink-soft: #555555;
    --band: #3b3b3b;
    --band-dark: #2a2a2a;
  }
  * { box-sizing: border-box; margin: 0; padding: 0; }
  html, body {
    width: 1200px; height: 900px; overflow: hidden;
    background: var(--page-bg);
  }
  body {
    display: flex; align-items: center; justify-content: center;
    font-family: "Michroma", sans-serif;
    color: var(--ink);
  }
  .business-card {
    position: relative;
    width: 1000px; height: 572px;
    background: var(--card-bg);
    border-radius: 10px;
    overflow: hidden;
    box-shadow: 0 2px 10px rgba(0,0,0,0.12);
  }
  .brand-block {
    position: absolute;
    left: 150px; top: 96px;
    display: flex; flex-direction: column; align-items: flex-start;
  }
  .brand-row { display: flex; align-items: center; gap: 16px; white-space: nowrap; }
  .brand-mark {
    width: 30px; height: 30px; flex: none;
    background: var(--ink);
  }
  .brand-name {
    font-size: 29px; letter-spacing: 1px;
    text-transform: uppercase; color: var(--ink);
    line-height: 1; white-space: nowrap;
  }
  .brand-tagline {
    margin-top: 16px; margin-left: 46px;
    font-size: 19px; letter-spacing: 1.5px;
    color: var(--ink-soft); white-space: nowrap;
  }
  .person {
    position: absolute; left: 455px; top: 250px;
  }
  .person-name {
    font-size: 22px; letter-spacing: 2px;
    text-transform: uppercase; color: var(--ink);
    white-space: nowrap;
  }
  .person-title {
    margin-top: 14px;
    font-size: 16px; letter-spacing: 2px;
    text-transform: uppercase; color: var(--ink-soft);
    white-space: nowrap;
  }
  .contact {
    position: absolute; left: 60px; top: 362px;
    font-size: 12.5px; letter-spacing: 1px;
    text-transform: uppercase; color: var(--ink);
  }
  .contact-line { display: flex; align-items: center; gap: 10px; height: 28px; white-space: nowrap; }
  .contact-line + .contact-line { margin-left: 12px; }
  .contact-icon { width: 16px; height: 16px; flex: none; }
  .contact-gap { width: 10px; }
  .footer-band {
    position: absolute; left: 0; right: 0; bottom: 0; height: 82px;
    background: var(--band-dark);
    border-top: 3px solid var(--band);
  }
  .footer-tab {
    position: absolute; left: 340px; bottom: 34px;
    width: 420px; height: 60px;
    background: var(--band);
    border-radius: 14px;
  }
</style>
</head>
<body>
  <div class="business-card">
    <div class="brand-block">
      <div class="brand-row">
        <div class="brand-mark"></div>
        <div class="brand-name">Brindlewood Terrain, LLC</div>
      </div>
      <div class="brand-tagline">Oil and Gas Land Services</div>
    </div>

    <div class="person">
      <div class="person-name">Gavin Ressler</div>
      <div class="person-title">Petroleum Landman</div>
    </div>

    <div class="contact">
      <div class="contact-line">
        <svg class="contact-icon" viewBox="0 0 16 16" aria-hidden="true"><circle cx="8" cy="8" r="8" fill="#2f2f2f"/><path d="M8 3.5a2.8 2.8 0 0 0-2.8 2.8C5.2 8.6 8 12 8 12s2.8-3.4 2.8-5.7A2.8 2.8 0 0 0 8 3.5z" fill="#fff"/><circle cx="8" cy="6.3" r="1" fill="#2f2f2f"/></svg>
        <span>426 West Orchard Lane North Canton, OH 44720</span>
        <span class="contact-gap"></span>
        <svg class="contact-icon" viewBox="0 0 16 16" aria-hidden="true"><circle cx="8" cy="8" r="8" fill="#2f2f2f"/><path d="M5.4 4h1.6l.8 2-1 .8a5 5 0 0 0 2.4 2.4l.8-1 2 .8v1.6c0 .4-.4.8-.8.8A7 7 0 0 1 4.6 4.8c0-.4.4-.8.8-.8z" fill="#fff"/></svg>
        <span>214-555-0193</span>
      </div>
      <div class="contact-line">
        <svg class="contact-icon" viewBox="0 0 16 16" aria-hidden="true"><circle cx="8" cy="8" r="8" fill="#2f2f2f"/><path d="M5.4 4h1.6l.8 2-1 .8a5 5 0 0 0 2.4 2.4l.8-1 2 .8v1.6c0 .4-.4.8-.8.8A7 7 0 0 1 4.6 4.8c0-.4.4-.8.8-.8z" fill="#fff"/></svg>
        <span>330-555-0147</span>
        <span class="contact-gap"></span>
        <svg class="contact-icon" viewBox="0 0 16 16" aria-hidden="true"><circle cx="8" cy="8" r="8" fill="#2f2f2f"/><rect x="4" y="5" width="8" height="6" rx="0.8" fill="#fff"/><path d="M4.3 5.4 8 8.3l3.7-2.9" stroke="#2f2f2f" stroke-width="0.9" fill="none"/></svg>
        <span>gavin.r.ressler@quellmail.net</span>
      </div>
    </div>

    <div class="footer-band"></div>
    <div class="footer-tab"></div>
  </div>
</body>
</html>
```